3D abstract logo Construction, Kitchen and Bath design and Project Management Business Card Design

I want a 3d abstract logo for a new General Construction, Kitchen and Bath design and Project Management Company located at Philadelphia PA, we want to put our logo in the white color trucks too. I want to look professional and serious at the same time look like an architect design and the warm originals color that make you feel in a nice decorated home, I like the colors trend in this link:
http://www.quillorbit.example/qo/kts/cardmaker.aspx?alt_doc_id=RM41T-K7B93-2W5&doc_id=5130948826&pf_id=H4D

I was thinking about a roof and the PA font could have square shape or like wood framing with two tones of the brick color black and creamy yellow color.... Also I like the keystone Idea like the modification or the LK Skyroute logo but curvy at the top

The final design should communicate big company (because we want to grow), responsible, professional and organized that really care about our customers and give them everything they need... plan and design, excellent labor and Project Management
Updates

I doesn't have to be 3d

Reason: I haven't received enough options...

Please stick with the warm tones shown in the image001 attached I like spicy cinnamon instead a cold wine or brick color and also the cream yellowish tones added

Hello designers, please use only the idea and colors of the image001 I don't want to be stick with a house logo because I do commercial construction too so I prefer work around the keystone idea maybe leaving the style of the PA.
I'd like the base tone on the card dark like first option and you can send me a white option too.

Please send me your ideas as soon as possible 

Thank you so much!

Target Market(s)

Builders, State, commercial business owners, Property owners or Real State and Property Management Companies

Industry/Entity Type

Architect

Contact Information for Business Card

LK Buildworks LLC
“Every build is our promise”
Renata Solvik Eng.
President
Commercial & Residential General Construction
Kitchen & Bath Design | Project Management
Phone: 215-738-4196 | Fax: 215-738-4197 Cell: 856-390-7712
renata@lkbuildworks.example

```html
<!DOCTYPE html>
<html lang="en">
<head>
<meta charset="utf-8">
<title>LK Buildworks LLC – Business Card</title>
<link rel="stylesheet" href="https://fonts.googleapis.com/css2?family=Jost:ital,wght@0,400;0,500;0,600;1,300;1,400;1,600;1,700&display=swap">
<style>
  :root {
    --cinnamon: #7d2420;
    --paper: #ffffff;
    --ink-light: #ffffff;
  }
  html, body {
    margin: 0;
    padding: 0;
    overflow: hidden;
    background: var(--paper);
  }
  .card {
    position: relative;
    width: 1200px;
    height: 702px;
    overflow: hidden;
    background: var(--paper);
    font-family: "Jost", "Futura", sans-serif;
  }
  .card__panel {
    position: absolute;
    inset: 0;
  }
  .brand {
    position: absolute;
    left: 40px;
    top: 60px;
    width: 350px;
    text-align: center;
  }
  .brand__square {
    display: block;
    width: 120px;
    height: 120px;
    margin: 40px auto 54px;
    background: var(--cinnamon);
  }
  .brand__name {
    margin: 0;
    font-size: 48px;
    font-weight: 500;
    color: var(--cinnamon);
    letter-spacing: 0.5px;
    white-space: nowrap;
  }
  .contact {
    position: absolute;
    left: 59px;
    top: 402px;
    margin: 0;
    color: var(--cinnamon);
    font-size: 25px;
    font-style: italic;
    font-weight: 400;
    line-height: 32px;
  }
  .contact__label { font-weight: 700; }
  .contact__web b { font-weight: 700; }
  .person {
    position: absolute;
    left: 616px;
    top: 54px;
    color: var(--ink-light);
  }
  .person__name {
    margin: 0;
    font-size: 60px;
    font-style: italic;
    font-weight: 700;
    line-height: 1;
    letter-spacing: 0.5px;
  }
  .person__title {
    margin: 8px 0 0;
    font-size: 44px;
    font-style: italic;
    font-weight: 400;
    line-height: 1.1;
  }
  .person__email {
    margin: 22px 0 0;
    font-size: 23px;
    font-style: italic;
    font-weight: 400;
  }
  .person__email b { font-weight: 700; }
  .company {
    position: absolute;
    left: 616px;
    top: 384px;
    color: var(--ink-light);
  }
  .company__name {
    margin: 0;
    font-size: 48px;
    font-style: italic;
    font-weight: 700;
    line-height: 1;
    letter-spacing: 0.5px;
  }
  .company__tagline {
    margin: 4px 0 0;
    font-size: 30px;
    font-style: italic;
    font-weight: 700;
    line-height: 1.2;
  }
  .company__services {
    margin: 12px 0 0;
    font-size: 21px;
    font-weight: 400;
    line-height: 23px;
  }
</style>
</head>
<body>
<main class="card">
  <svg class="card__panel" width="1200" height="702" viewBox="0 0 1200 702" aria-hidden="true">
    <polygon points="586,0 1200,0 1200,702 306,702" fill="var(--cinnamon)"/>
  </svg>

  <div class="brand">
    <span class="brand__square"></span>
    <p class="brand__name">LK Buildworks</p>
  </div>

  <p class="contact">
    <span class="contact__label">Phone:</span> 215-738-4196<br>
    <span class="contact__label">Fax:</span> 215-738-4197<br>
    <span class="contact__label">Cell:</span> 856-390-7712<br>
    <span class="contact__web">www.<b>lkbuildworks</b>.example</span>
  </p>

  <section class="person">
    <h1 class="person__name">Renata Solvik</h1>
    <p class="person__title">President</p>
    <p class="person__email"><b>renata@lkbuildworks</b>.example</p>
  </section>

  <section class="company">
    <h2 class="company__name">LK Buildworks LLC</h2>
    <p class="company__tagline">“Every build is our promise”</p>
    <p class="company__services">Commercial &amp; Residential General Construction<br>Kitchen &amp; Bath Design &nbsp;|&nbsp; Project Management</p>
  </section>
</main>
</body>
</html>
```